Graphics for a 'Pick the Hue' mobile phone project

I need the graphics (including source graphics in Illustrator or Photoshop) for the screens inside the game.

Please read the attached brief carefully, thanks!

```html
<!DOCTYPE html>
<html lang="en">
<head>
<meta charset="utf-8">
<title>Pick the Hue – Home</title>
<link rel="stylesheet" href="https://fonts.googleapis.com/css2?family=Montserrat:wght@700&display=swap">
<style>
  :root {
    --bg-center: #f4f4f4;
    --bg-edge: #d6d6d6;
    --teal: #22bb9c;
    --teal-dark: #1a8f77;
    --ink: #111111;
    --white: #ffffff;
    --trophy: #1f68b4;
    --settings: #22a8c8;
    --games: #ef8e3a;
    --shop: #dc1a70;
    --sound: #e94a4c;
    --ad-green: #00704a;
    --mascot-main: #8a5a2b;
    --mascot-dark: #5a3a1c;
    --ad-photo-top: #3b3b3b;
    --ad-photo-bottom: #1f4a3a;
  }
  * { margin: 0; padding: 0; box-sizing: border-box; }
  html, body { width: 720px; height: 1200px; overflow: hidden; }
  body {
    position: relative;
    background: radial-gradient(ellipse at 50% 45%, var(--bg-center) 0%, var(--bg-center) 35%, var(--bg-edge) 100%);
    font-family: "Montserrat", Arial, sans-serif;
    font-weight: 700;
  }
  .game-title {
    position: absolute;
    top: 196px;
    left: 0;
    width: 720px;
    text-align: center;
    color: var(--ink);
    font-size: 120px;
    line-height: 142px;
    letter-spacing: -2px;
  }
  .credit {
    position: absolute; top: 510px; width: 100%;
    text-align: center;
    font-size: 31px; color: var(--ink);
  }
  .mascot {
    position: absolute; left: 365px; top: 606px;
    width: 235px; height: 260px;
    background: linear-gradient(180deg, var(--mascot-main), var(--mascot-dark));
    border-radius: 46% 46% 30% 30%;
  }
  .play-button {
    position: absolute; left: 223px; top: 760px;
    width: 247px; height: 106px;
    border-radius: 8px;
    background: linear-gradient(155deg, var(--teal) 55%, #1fa98d 55%);
    box-shadow: inset 0 -8px 0 var(--teal-dark);
    color: var(--white);
    font-size: 62px; line-height: 92px; text-align: center;
  }
  .menu {
    position: absolute; top: 933px; left: 63px;
    display: flex; gap: 33px;
  }
  .menu-tile {
    width: 90px; height: 95px; border-radius: 4px;
    display: flex; align-items: center; justify-content: center;
    padding-bottom: 6px;
    box-shadow: inset 0 -7px 0 rgba(0,0,0,0.22);
  }
  .menu-tile svg { width: 54px; height: 54px; }
  .tile-trophy { background: var(--trophy); }
  .tile-settings { background: var(--settings); }
  .tile-games { background: var(--games); }
  .tile-shop { background: var(--shop); }
  .tile-sound { background: var(--sound); }
  .ad-banner {
    position: absolute; left: 0; top: 1113px;
    width: 720px; height: 87px;
    background: var(--ad-green); color: var(--white);
  }
  .ad-brand {
    position: absolute; left: 26px; top: 14px;
    font-size: 28px; letter-spacing: 2px;
  }
  .ad-tagline {
    position: absolute; left: 300px; top: 19px;
    font-size: 22px;
  }
  .ad-line {
    position: absolute; left: 26px; top: 50px;
    font-size: 22px;
  }
  .ad-photo {
    position: absolute; right: 0; top: 0;
    width: 130px; height: 87px;
    background: linear-gradient(180deg, var(--ad-photo-top), var(--ad-photo-bottom));
  }
</style>
</head>
<body>
  <h1 class="game-title">Pick<br>the Hue</h1>
  <p class="credit">by Marco Ellison</p>

  <div class="mascot" role="img" aria-label="Cartoon brown puppy mascot peeking over the play button"></div>
  <div class="play-button">play</div>

  <nav class="menu">
    <div class="menu-tile tile-trophy" aria-label="Leaderboard">
      <svg viewBox="0 0 54 54" fill="#e8e8e8"><path d="M14 8h26v10c0 9-6 15-13 15S14 27 14 18z"/><path d="M14 11H6v5c0 6 5 10 10 10v-4c-4 0-6-3-6-6v-1h4zM40 11h8v5c0 6-5 10-10 10v-4c4 0 6-3 6-6v-1h-4z"/><rect x="24" y="32" width="6" height="8"/><rect x="16" y="40" width="22" height="6" rx="1"/></svg>
    </div>
    <div class="menu-tile tile-settings" aria-label="Settings">
      <svg viewBox="0 0 54 54"><g fill="#ffffff"><circle cx="27" cy="27" r="15"/><g><rect x="22" y="4" width="10" height="10" rx="2"/><rect x="22" y="40" width="10" height="10" rx="2"/><rect x="4" y="22" width="10" height="10" rx="2"/><rect x="40" y="22" width="10" height="10" rx="2"/></g><g transform="rotate(45 27 27)"><rect x="22" y="4" width="10" height="10" rx="2"/><rect x="22" y="40" width="10" height="10" rx="2"/><rect x="4" y="22" width="10" height="10" rx="2"/><rect x="40" y="22" width="10" height="10" rx="2"/></g></g><circle cx="27" cy="27" r="6" fill="#22a8c8"/></svg>
    </div>
    <div class="menu-tile tile-games" aria-label="More games">
      <svg viewBox="0 0 54 54"><path d="M12 16h30c6 0 9 8 9 17 0 7-6 9-10 4l-5-6H18l-5 6c-4 5-10 3-10-4 0-9 3-17 9-17z" fill="#ffffff"/><g fill="#ef8e3a"><rect x="11" y="22" width="10" height="3"/><rect x="14.5" y="18.5" width="3" height="10"/><circle cx="36" cy="21" r="2"/><circle cx="41" cy="25" r="2"/></g></svg>
    </div>
    <div class="menu-tile tile-shop" aria-label="Shop">
      <svg viewBox="0 0 54 54" fill="none" stroke="#ffffff" stroke-width="4" stroke-linejoin="round"><path d="M4 10h7l6 24h26l5-17H13"/><circle cx="20" cy="43" r="3" fill="#ffffff"/><circle cx="39" cy="43" r="3" fill="#ffffff"/></svg>
    </div>
    <div class="menu-tile tile-sound" aria-label="Sound">
      <svg viewBox="0 0 54 54"><path d="M6 20h9l13-11v36L15 34H6z" fill="#ffffff"/><g fill="none" stroke="#ffffff" stroke-width="3.5" stroke-linecap="round"><path d="M34 21c3 3 3 9 0 12"/><path d="M39 16c6 6 6 16 0 22"/><path d="M44 11c9 9 9 23 0 32"/></g></svg>
    </div>
  </nav>

  <aside class="ad-banner">
    <div class="ad-brand">BREWHAVEN</div>
    <div class="ad-tagline">Pandu-Lalu</div>
    <div class="ad-line">Kini Dibuka di Mercato Plus Taman Seri Mall</div>
    <div class="ad-photo" role="img" aria-label="Photo of a café barista holding a drink"></div>
  </aside>
</body>
</html>
```